BRVL Brochure Design

Northfield Council of Clinical Standards (BRVL) needs a whole new brochure. I've upload EPS logos and past brochures. Our tagline is to "modernize healthcare" and we think our brochure should reflect that, so that's the purpose of this project.

BRVL is a proven leader in healthcare education, training and
consulting services for health professionals. We’ve earned a reputation for excellence in healthcare quality improvement and management.

BRVL works to improve healthcare quality by educating healthcare professionals about healthcare best practices. We focus on instructing our clients on how to plan for, measure, and improve healthcare quality in all facilities and facets such as:

Patient Safety
Infection Control
Performance Improvement
Risk Management
Compliance and Accreditation
Health and Hospital Administration
Health Insurance
Healthcare Financial Management
Facility Management and Safety

DESIGN SUGGESTIONS:

Brochure Size: 8.5 X 11 full size brochure or 8.5 X 11 trifold brochure

Number of Pages: 2 to 3

Colors: Feel free to use a wide array of colors but try to stay away from colors that are too loud, ex: Pink, Purple, Neon Green.

Themes: Professional, Educational

Designs:

Pelor by Oskar Lindqvist

Quorvo Pamphlet by Derek Malloway

Lanterns for harvest by Solvendri

Paisaje de Sr KT by vrpl

http://www.plimbask.com/post/28461937205/10-creative-brochure-designs

Don't limit yourself to these examples. However, these are examples we liked

Reason: We would like to see more designs

We want more full page designs than tri-fold 

We are considering both tri-fold and full-page but would like to see more full page designs 

Reason: Our lead designer making the decisions on this project has been fired. I apologize for the inconvenience. We want extend the project one last time

Target Market(s)

Students, Doctors, and Educational Professionals

Industry/Entity Type

Healthcare

Logo Text

asdfasdf

Font styles to use
Serif
Sans Serif
Decorative
Script

Requirements
Should not have
• Pink, Purple, Neon Green colors

```html
<!DOCTYPE html>
<html lang="en">
<head>
<meta charset="utf-8">
<title>BRVL Trifold Brochure</title>
<link href="https://fonts.googleapis.com/css2?family=Tinos:wght@400;700&display=swap" rel="stylesheet">
<style>
  :root{
    --stage:#e4e6ea;
    --blue-deep:#0a3a86;
    --blue:#1560bd;
    --blue-bright:#2b8de2;
    --blue-pale:#cfe3f6;
    --silver-light:#ffffff;
    --silver:#d9dee4;
    --ink:#1d2733;
    --white:#ffffff;
  }
  *{box-sizing:border-box;margin:0;padding:0}
  html,body{width:1200px;height:626px;overflow:hidden}
  body{background:var(--stage);font-family:"Tinos",serif;color:var(--ink);position:relative}
  .brochure{position:absolute;left:210px;top:23px;width:780px;height:580px;display:flex;box-shadow:0 4px 18px rgba(0,0,0,.18)}
  .panel{position:relative;width:260px;height:580px;overflow:hidden;
    background:linear-gradient(180deg,var(--silver-light) 0%,#eef1f4 45%,var(--silver) 100%)}
  .panel + .panel{border-left:1px solid rgba(0,0,0,.06)}
  .panel svg.shapes{position:absolute;left:0;top:0}

  .tab{position:absolute;left:0;height:28px;padding:0 26px 0 16px;display:flex;align-items:center;
    color:var(--white);font-weight:700;font-size:17px;letter-spacing:.3px;
    background:var(--blue-deep);clip-path:polygon(0 0,100% 0,88% 100%,0 100%)}
  .tab-mission{top:38px}
  .tab-values{top:352px}
  .tab-rule{position:absolute;left:150px;width:98px;height:2px;background:var(--blue-deep)}
  .tab-rule::after{content:"";position:absolute;right:-3px;top:-2px;width:6px;height:6px;border-radius:50%;background:var(--blue-deep)}

  .photo-round{position:absolute;border-radius:50%;border:4px solid var(--white);box-shadow:0 0 0 4px var(--blue)}
  .photo-staff{top:100px;width:100px;height:100px;
    background:radial-gradient(circle at 50% 40%,#e9eef3 0%,#b9cde3 55%,#6f9ac8 100%)}
  .photo-staff.one{left:20px}
  .photo-staff.two{left:132px}

  .mission-text{position:absolute;left:14px;top:220px;width:236px;font-size:13.4px;line-height:16px}
  .values-list{position:absolute;left:14px;top:395px;width:236px;list-style:none}
  .values-list li{position:relative;padding-left:20px;font-size:13px;line-height:16px;text-transform:uppercase;margin-bottom:10px}
  .values-list li:nth-child(4){margin-top:10px}
  .values-list svg{position:absolute;left:0;top:1px}

  .placeholder-instrument{position:absolute;left:10px;top:0;width:200px;height:220px;
    background:radial-gradient(ellipse at 45% 40%,rgba(190,198,206,.55) 0%,rgba(230,233,237,.2) 60%,rgba(255,255,255,0) 75%)}

  .brand{position:absolute;display:flex;align-items:center;gap:7px;color:var(--blue-deep);font-weight:700}
  .brand-dot{width:34px;height:34px;border-radius:50%;background:var(--blue-deep)}
  .brand-name{font-size:38px;line-height:1}
  .brand-full{font-size:8px;line-height:9px;width:82px}
  .brand-center{left:18px;top:245px}
  .brand-cover{left:22px;top:30px}

  .address-badge{position:absolute;left:43px;top:327px;width:166px;height:42px;border-radius:4px;
    background:linear-gradient(180deg,var(--blue-bright),var(--blue));color:var(--white);
    font-weight:700;font-size:26px;display:flex;align-items:center;justify-content:center;box-shadow:0 2px 4px rgba(0,0,0,.25)}
  .address-badge::after{content:"";position:absolute;left:50%;bottom:-8px;margin-left:-8px;border:8px solid transparent;border-bottom:0;border-top-color:var(--blue)}
  .contact{position:absolute;left:0;top:385px;width:260px;text-align:center;color:var(--white);font-size:12.4px;line-height:17px}
  .contact .gap{margin-top:8px}
  .contact .phone{font-weight:700;font-size:15px;display:inline-flex;align-items:center;gap:5px;margin-top:10px}
  .contact strong{font-weight:700}

  .photo-care{position:absolute;left:11px;top:191px;width:266px;height:266px;border-radius:50%;
    border:6px solid var(--white);
    background:radial-gradient(circle at 45% 45%,#f3f1ee 0%,#d7dde6 40%,#7d9cc8 75%,#4d6fa4 100%)}
  .tagline{position:absolute;left:0;width:260px;text-align:center;color:var(--white);font-weight:400}
  .tagline-main{top:470px;font-size:42px;line-height:44px}
  .tagline-sub{top:512px;font-size:27px;line-height:30px}
</style>
</head>
<body>
<main class="brochure">

  <section class="panel panel-mission">
    <svg class="shapes" width="260" height="580" viewBox="0 0 260 580" aria-hidden="true">
      <defs>
        <linearGradient id="missionBand" x1="0" y1="0" x2="1" y2="1">
          <stop offset="0" stop-color="#0a3a86"/>
          <stop offset="0.6" stop-color="#1f78d2"/>
          <stop offset="1" stop-color="#cfe3f6"/>
        </linearGradient>
      </defs>
      <path d="M0 0 H260 V120 Q150 180 0 150 Z" fill="url(#missionBand)"/>
      <path d="M0 150 Q150 180 260 120 V132 Q150 196 0 164 Z" fill="#ffffff" opacity=".7"/>
      <rect x="0" y="562" width="260" height="18" fill="#1560bd"/>
    </svg>
    <h2 class="tab tab-mission">OUR MISSION</h2>
    <div class="photo-round photo-staff one" role="img" aria-label="Photo of a smiling nurse with colleagues"></div>
    <div class="photo-round photo-staff two" role="img" aria-label="Photo of a doctor reviewing notes with a colleague"></div>
    <p class="mission-text">Our mission is to enhance quality in healthcare by transforming the professionals who work in healthcare.We aim to give you the tools and knowledge that you need to impact healthcare delivery and outcomes and to be an advocate for quality and patient safety.</p>
    <h2 class="tab tab-values">OUR VALUES</h2>
    <span class="tab-rule" style="top:376px"></span>
    <ul class="values-list">
      <li><svg width="14" height="14" viewBox="0 0 14 14" aria-hidden="true"><circle cx="7" cy="7" r="6.5" fill="#1560bd"/><path d="M3.8 7.2l2.2 2.2 4.2-4.6" stroke="#fff" stroke-width="1.6" fill="none"/></svg>Quality in all that we do and offer</li>
      <li><svg width="14" height="14" viewBox="0 0 14 14" aria-hidden="true"><circle cx="7" cy="7" r="6.5" fill="#1560bd"/><path d="M3.8 7.2l2.2 2.2 4.2-4.6" stroke="#fff" stroke-width="1.6" fill="none"/></svg>Integrity in all of our work</li>
      <li><svg width="14" height="14" viewBox="0 0 14 14" aria-hidden="true"><circle cx="7" cy="7" r="6.5" fill="#1560bd"/><path d="M3.8 7.2l2.2 2.2 4.2-4.6" stroke="#fff" stroke-width="1.6" fill="none"/></svg>Innovations in training and education</li>
      <li><svg width="14" height="14" viewBox="0 0 14 14" aria-hidden="true"><circle cx="7" cy="7" r="6.5" fill="#1560bd"/><path d="M3.8 7.2l2.2 2.2 4.2-4.6" stroke="#fff" stroke-width="1.6" fill="none"/></svg>Leadership worldwide</li>
      <li><svg width="14" height="14" viewBox="0 0 14 14" aria-hidden="true"><circle cx="7" cy="7" r="6.5" fill="#1560bd"/><path d="M3.8 7.2l2.2 2.2 4.2-4.6" stroke="#fff" stroke-width="1.6" fill="none"/></svg>Continuous education</li>
    </ul>
  </section>

  <section class="panel panel-contact">
    <div class="placeholder-instrument" role="img" aria-label="Faint photo of a stethoscope"></div>
    <svg class="shapes" width="260" height="580" viewBox="0 0 260 580" aria-hidden="true">
      <defs>
        <linearGradient id="contactBand" x1="0" y1="0" x2="0" y2="1">
          <stop offset="0" stop-color="#1f78d2"/>
          <stop offset="1" stop-color="#0a3a86"/>
        </linearGradient>
      </defs>
      <path d="M0 296 Q120 330 260 300 V580 H0 Z" fill="#cfe3f6"/>
      <path d="M0 306 Q120 342 260 312 V580 H0 Z" fill="url(#contactBand)"/>
    </svg>
    <div class="brand brand-center">
      <span class="brand-dot"></span>
      <span class="brand-name">BRVL</span>
      <span class="brand-full">Northfield Council of Clinical Standards</span>
    </div>
    <div class="address-badge">Address</div>
    <address class="contact" style="font-style:normal">
      <div>Dr. Helen Ostrand, Executive Director</div>
      <div>The Northfield Council of Clinical Standards</div>
      <div class="gap">2807 Marlowe Ave</div>
      <div>Brenton City, Kestrel 60417</div>
      <div class="phone"><svg width="14" height="14" viewBox="0 0 14 14" aria-hidden="true"><rect x="0" y="0" width="14" height="14" rx="2" fill="#fff"/><path d="M4 3.2c.6-.4 1.1-.2 1.4.4l.6 1.2c.2.5 0 .9-.4 1.2l-.4.3c.5 1 1.3 1.8 2.3 2.3l.3-.4c.3-.4.7-.6 1.2-.4l1.2.6c.6.3.8.8.4 1.4-.6.9-1.6 1.2-2.6.8C6 9.8 4.2 8 3.4 5.8c-.4-1 0-2 .6-2.6z" fill="#1560bd"/></svg>(555)-014-2290</div>
      <div>Fax:(555)-014-2290</div>
      <div>Email: info@brvl.org</div>
      <div>Website: <strong>www.brvl.org</strong></div>
    </address>
  </section>

  <section class="panel panel-cover">
    <svg class="shapes" width="260" height="580" viewBox="0 0 260 580" aria-hidden="true">
      <defs>
        <linearGradient id="coverBand" x1="0" y1="0" x2="1" y2="1">
          <stop offset="0" stop-color="#0a3a86"/>
          <stop offset="0.55" stop-color="#1560bd"/>
          <stop offset="1" stop-color="#2b8de2"/>
        </linearGradient>
      </defs>
      <path d="M0 150 Q130 100 260 140 V160 Q130 120 0 172 Z" fill="#2b8de2"/>
      <path d="M0 380 Q40 470 260 430 V580 H0 Z" fill="url(#coverBand)"/>
      <path d="M0 470 Q130 440 260 470" stroke="#5aa8ea" stroke-width="1" fill="none" opacity=".6"/>
      <circle cx="144" cy="324" r="144" fill="none" stroke="#1560bd" stroke-width="6"/>
    </svg>
    <div class="brand brand-cover">
      <span class="brand-dot"></span>
      <span class="brand-name">BRVL</span>
      <span class="brand-full">Northfield Council of Clinical Standards</span>
    </div>
    <div class="photo-care" role="img" aria-label="Photo of a doctor holding the hand of a smiling older patient"></div>
    <h1 class="tagline tagline-main">Modernize</h1>
    <p class="tagline tagline-sub">healthcare</p>
  </section>

</main>
</body>
</html>
```